60 Ways to de-stress Poster

I would like a poster ( A4 full colour) with a list of 60 ways to destress. I would like the design to be clean and stylish (not cartoonish)

My Target market is stressed out mums so I want the poster to feel inspirational and relaxing to look at.

I have added a sample of something I like - but open to other ideas

Finished art would be print ready pdf

Target Market(s)

Mums who are stressed out - mainly new mums. I want this to be a poster that someone would happily put up that looks more like artwork.

Requirements
Must have
• My logo elements and colours but happy to incorporate other colours that blend well into it.

Colours:
Bright green: Pantone 376
Bright green as CMYK: c: 45.2% m: 0% y: 100% k: 0%

Logo text large grey: 70% black
Logo text strapline: 75% black
Tree: 80% black

Fonts:
Logo 'Willowbank Haven': Verdana
Logo 'Counselling & coaching services for mums': Gill Sans Light
Should not have
• No cartoonish images - I want it very clean and stylish

```html
<!DOCTYPE html>
<html lang="en">
<head>
<meta charset="utf-8">
<title>60 Ways to De-Stress – Willowbank Haven</title>
<link rel="stylesheet" href="https://fonts.googleapis.com/css2?family=Oswald:wght@300;500;700&family=Questrial&display=swap">
<style>
  :root {
    --page: #ffffff;
    --paper: #f9dcc6;
    --green: #9dc42a;
    --leaf: #4aaa3c;
    --lime: #a9c833;
    --sage: #87a07a;
    --red: #e7452d;
    --pink: #ec6d98;
    --orange: #f3a65a;
    --blue: #39a6de;
    --grey: #6d6e70;
    --brown: #7b4e2b;
  }
  html, body {
    margin: 0;
    width: 1000px;
    height: 1200px;
    overflow: hidden;
    background: var(--page);
  }
  .poster { display: block; width: 1000px; height: 1200px; }
  .poster-sheet { fill: var(--paper); }

  .round   { font-family: "Questrial", "Century Gothic", sans-serif; }
  .bold    { font-family: "Oswald", "Arial Narrow", sans-serif; font-weight: 700; }
  .medium  { font-family: "Oswald", "Arial Narrow", sans-serif; font-weight: 500; }
  .light   { font-family: "Oswald", "Arial Narrow", sans-serif; font-weight: 300; }

  .c-green  { fill: var(--green); }
  .c-leaf   { fill: var(--leaf); }
  .c-lime   { fill: var(--lime); }
  .c-sage   { fill: var(--sage); }
  .c-red    { fill: var(--red); }
  .c-pink   { fill: var(--pink); }
  .c-orange { fill: var(--orange); }
  .c-blue   { fill: var(--blue); }
  .c-grey   { fill: var(--grey); }
  .c-brown  { fill: var(--brown); }

  .brand-mark { fill: var(--grey); }
</style>
</head>
<body>
<svg class="poster" viewBox="0 0 1000 1200" xmlns="http://www.w3.org/2000/svg" role="img" aria-label="60 ways to de-stress poster">
  <rect class="poster-sheet" x="127" y="62" width="746" height="1075"/>

  <g class="poster-title">
    <text class="round c-green" x="152" y="116" font-size="52" textLength="696" lengthAdjust="spacingAndGlyphs">60 WAYS TO DE-STRESS</text>
  </g>

  <g class="ways" lengthAdjust="spacingAndGlyphs">
    <text class="bold c-red" x="152" y="148" font-size="27" textLength="238" lengthAdjust="spacingAndGlyphs">EAT SOMETHING MINDFULLY</text>
    <text class="round c-pink" x="398" y="147" font-size="25" textLength="165" lengthAdjust="spacingAndGlyphs">VISIT A FARMERS</text>
    <text class="round c-pink" x="398" y="187" font-size="50" textLength="165" lengthAdjust="spacingAndGlyphs">MARKET</text>
    <text class="light c-grey" x="568" y="200" font-size="98" textLength="100" lengthAdjust="spacingAndGlyphs">VENT</text>
    <text class="round c-blue" x="675" y="160" font-size="42" textLength="170" lengthAdjust="spacingAndGlyphs">LISTEN TO</text>
    <text class="round c-blue" x="675" y="210" font-size="60" textLength="173" lengthAdjust="spacingAndGlyphs">MUSIC</text>
    <text class="round c-orange" x="152" y="183" font-size="25" textLength="238" lengthAdjust="spacingAndGlyphs">MAKE A GRATITUDE LIST</text>

    <text class="round c-blue" x="152" y="228" font-size="40" textLength="126" lengthAdjust="spacingAndGlyphs">GO TO THE</text>
    <text class="round c-grey" x="286" y="214" font-size="34" textLength="234" lengthAdjust="spacingAndGlyphs">HUG SOMEONE</text>
    <text class="round c-red" x="286" y="243" font-size="31" textLength="239" lengthAdjust="spacingAndGlyphs">LIGHT A SCENTED</text>
    <text class="round c-blue" x="150" y="293" font-size="86" textLength="130" lengthAdjust="spacingAndGlyphs">PARK</text>
    <text class="round c-red" x="286" y="296" font-size="74" textLength="241" lengthAdjust="spacingAndGlyphs">CANDLE</text>
    <text class="round c-green" x="535" y="248" font-size="43" textLength="122" lengthAdjust="spacingAndGlyphs">HAVE A</text>
    <text class="round c-green" x="535" y="296" font-size="63" textLength="125" lengthAdjust="spacingAndGlyphs">BATH</text>
    <text class="round c-green" x="665" y="244" font-size="37" textLength="143" lengthAdjust="spacingAndGlyphs">PAINT A</text>
    <text class="round c-green" x="665" y="270" font-size="31" textLength="143" lengthAdjust="spacingAndGlyphs">PICTURE</text>
    <text class="round c-brown" x="665" y="291" font-size="23" textLength="143" lengthAdjust="spacingAndGlyphs">PLAY A GAME</text>
    <text class="bold c-orange" transform="translate(848 580) rotate(-90)" x="0" y="0" font-size="44" textLength="365" lengthAdjust="spacingAndGlyphs">WATCH A FUNNY MOVIE</text>

    <text class="bold c-sage" x="152" y="329" font-size="33" textLength="335" lengthAdjust="spacingAndGlyphs">BUY YOURSELF FLOWERS</text>
    <text class="medium c-grey" x="494" y="328" font-size="30" textLength="111" lengthAdjust="spacingAndGlyphs">ASK FOR HELP</text>
    <text class="round c-grey" x="610" y="312" font-size="25" textLength="196" lengthAdjust="spacingAndGlyphs">COMPLIMENT</text>
    <text class="round c-grey" x="615" y="335" font-size="25" textLength="191" lengthAdjust="spacingAndGlyphs">YOURSELF</text>
    <text class="round c-grey" x="612" y="377" font-size="52" textLength="194" lengthAdjust="spacingAndGlyphs">OFTEN</text>
    <text class="bold c-lime" x="152" y="371" font-size="47" textLength="335" lengthAdjust="spacingAndGlyphs">TAKE SOME DEEP BREATHS</text>
    <text class="round c-orange" x="494" y="355" font-size="28" textLength="110" lengthAdjust="spacingAndGlyphs">GAZE AT</text>
    <text class="round c-orange" x="494" y="375" font-size="20" textLength="110" lengthAdjust="spacingAndGlyphs">THE STARS</text>

    <text class="bold c-brown" x="152" y="425" font-size="44" textLength="203" lengthAdjust="spacingAndGlyphs">TAKE A MINI</text>
    <text class="bold c-red" x="361" y="422" font-size="41" textLength="445" lengthAdjust="spacingAndGlyphs">WRITE POSITIVE SELF-STATEMENTS</text>
    <text class="bold c-brown" x="152" y="456" font-size="33" textLength="203" lengthAdjust="spacingAndGlyphs">MENTAL HOLIDAY</text>
    <text class="round c-pink" x="361" y="442" font-size="13" textLength="117" lengthAdjust="spacingAndGlyphs">PUT ON SOME MUSIC</text>
    <text class="round c-pink" x="361" y="457" font-size="16" textLength="117" lengthAdjust="spacingAndGlyphs">AND DANCE</text>
    <text class="bold c-blue" x="484" y="456" font-size="33" textLength="322" lengthAdjust="spacingAndGlyphs">SCALE DOWN YOUR TO DO LIST</text>

    <text class="medium c-leaf" transform="translate(187 468) rotate(90)" x="0" y="0" font-size="34" textLength="55" lengthAdjust="spacingAndGlyphs">FAKE A</text>
    <text class="medium c-leaf" transform="translate(151 466) rotate(90)" x="0" y="0" font-size="42" textLength="114" lengthAdjust="spacingAndGlyphs">SMILE</text>
    <text class="round c-blue" x="217" y="500" font-size="40" textLength="205" lengthAdjust="spacingAndGlyphs">BAKE SOME</text>
    <text class="round c-blue" x="217" y="547" font-size="60" textLength="207" lengthAdjust="spacingAndGlyphs">COOKIES</text>
    <text class="round c-grey" x="217" y="578" font-size="34" textLength="235" lengthAdjust="spacingAndGlyphs">WRITE A POEM</text>
    <text class="round c-sage" x="430" y="497" font-size="36" textLength="102" lengthAdjust="spacingAndGlyphs">GO FOR A</text>
    <text class="light c-sage" x="430" y="547" font-size="64" textLength="102" lengthAdjust="spacingAndGlyphs">WALK</text>
    <text class="medium c-brown" transform="translate(550 548) rotate(-90)" x="0" y="0" font-size="16" textLength="78" lengthAdjust="spacingAndGlyphs">CALL OR VISIT</text>
    <text class="medium c-brown" transform="translate(564 522) rotate(-90)" x="0" y="0" font-size="16" textLength="54" lengthAdjust="spacingAndGlyphs">A FRIEND</text>
    <text class="round c-pink" x="582" y="488" font-size="23" textLength="170" lengthAdjust="spacingAndGlyphs">SWING ON A</text>
    <text class="round c-pink" x="582" y="511" font-size="32" textLength="170" lengthAdjust="spacingAndGlyphs">SWING</text>
    <text class="round c-green" x="584" y="546" font-size="43" textLength="168" lengthAdjust="spacingAndGlyphs">MEDITATE</text>
    <text class="medium c-red" transform="translate(772 577) rotate(-90)" x="0" y="0" font-size="20" textLength="107" lengthAdjust="spacingAndGlyphs">CREATE SOME</text>
    <text class="medium c-red" transform="translate(808 577) rotate(-90)" x="0" y="0" font-size="40" textLength="107" lengthAdjust="spacingAndGlyphs">ROUTINES</text>
    <text class="round c-lime" x="467" y="578" font-size="31" textLength="285" lengthAdjust="spacingAndGlyphs">PLAY IN THE PARK</text>

    <text class="round c-pink" x="152" y="612" font-size="37" textLength="330" lengthAdjust="spacingAndGlyphs">FORGIVE SOMEONE</text>
    <text class="bold c-sage" x="490" y="612" font-size="33" textLength="356" lengthAdjust="spacingAndGlyphs">REVIEW YOUR ACHIEVEMENTS</text>
    <text class="round c-red" x="152" y="646" font-size="34" textLength="231" lengthAdjust="spacingAndGlyphs">STAND UP AND</text>
    <text class="round c-red" x="152" y="697" font-size="60" textLength="231" lengthAdjust="spacingAndGlyphs">STRETCH</text>
    <text class="round c-leaf" x="390" y="648" font-size="43" textLength="160" lengthAdjust="spacingAndGlyphs">PLANT A</text>
    <text class="round c-leaf" x="390" y="698" font-size="66" textLength="162" lengthAdjust="spacingAndGlyphs">TREE</text>
    <text class="round c-grey" x="556" y="646" font-size="40" textLength="290" lengthAdjust="spacingAndGlyphs">GET A HAIRCUT</text>
    <text class="round c-lime" x="557" y="670" font-size="28" textLength="163" lengthAdjust="spacingAndGlyphs">VOLUNTEER</text>
    <text class="round c-lime" x="557" y="694" font-size="28" textLength="163" lengthAdjust="spacingAndGlyphs">YOUR TIME</text>
    <text class="round c-brown" x="728" y="670" font-size="26" textLength="118" lengthAdjust="spacingAndGlyphs">WRITE IN A</text>
    <text class="round c-brown" x="728" y="694" font-size="26" textLength="118" lengthAdjust="spacingAndGlyphs">JOURNAL</text>

    <text class="bold c-grey" x="152" y="729" font-size="30" textLength="166" lengthAdjust="spacingAndGlyphs">RELIVE HAPPY</text>
    <text class="bold c-grey" x="152" y="768" font-size="47" textLength="166" lengthAdjust="spacingAndGlyphs">MEMORIES</text>
    <text class="bold c-lime" x="323" y="729" font-size="30" textLength="122" lengthAdjust="spacingAndGlyphs">PAT A DOG</text>
    <text class="medium c-orange" x="450" y="729" font-size="30" textLength="186" lengthAdjust="spacingAndGlyphs">GET A MASSAGE</text>
    <text class="bold c-red" x="648" y="729" font-size="30" textLength="198" lengthAdjust="spacingAndGlyphs">GO ON A PICNIC</text>
    <text class="bold c-brown" x="323" y="763" font-size="33" textLength="243" lengthAdjust="spacingAndGlyphs">PERFORM  AN ACT</text>
    <text class="bold c-brown" x="323" y="807" font-size="50" textLength="243" lengthAdjust="spacingAndGlyphs">OF KINDNESS</text>
    <text class="round c-sage" transform="translate(590 780) rotate(-90)" x="0" y="0" font-size="26" textLength="46" lengthAdjust="spacingAndGlyphs">TAKE</text>
    <text class="round c-sage" transform="translate(612 808) rotate(-90)" x="0" y="0" font-size="24" textLength="48" lengthAdjust="spacingAndGlyphs">A NAP</text>
    <text class="round c-leaf" x="648" y="758" font-size="28" textLength="198" lengthAdjust="spacingAndGlyphs">GIVE YOURSELF A</text>
    <text class="round c-leaf" x="647" y="808" font-size="57" textLength="199" lengthAdjust="spacingAndGlyphs">TIME-OUT</text>
    <text class="round c-lime" x="155" y="785" font-size="17" textLength="160" lengthAdjust="spacingAndGlyphs">BORROW A BOOK</text>
    <text class="round c-lime" x="155" y="806" font-size="16" textLength="160" lengthAdjust="spacingAndGlyphs">FROM THE LIBRARY</text>

    <text class="light c-sage" x="152" y="863" font-size="56" textLength="276" lengthAdjust="spacingAndGlyphs">OUTSOURCE IF YOU CAN</text>
    <text class="bold c-leaf" x="434" y="840" font-size="28" textLength="98" lengthAdjust="spacingAndGlyphs">LIVE FOR</text>
    <text class="bold c-leaf" x="434" y="866" font-size="33" textLength="98" lengthAdjust="spacingAndGlyphs">TODAY</text>
    <text class="medium c-red" x="537" y="836" font-size="22" textLength="146" lengthAdjust="spacingAndGlyphs">TRY PROGRESSIVE</text>
    <text class="medium c-red" x="537" y="886" font-size="61" textLength="146" lengthAdjust="spacingAndGlyphs">MUSCLE</text>
    <text class="medium c-red" x="537" y="926" font-size="41" textLength="146" lengthAdjust="spacingAndGlyphs">RELAXATION</text>
    <text class="round c-blue" transform="translate(716 928) rotate(-90)" x="0" y="0" font-size="40" textLength="110" lengthAdjust="spacingAndGlyphs">ACCEPT</text>
    <text class="round c-blue" transform="translate(735 888) rotate(-90)" x="0" y="0" font-size="20" textLength="70" lengthAdjust="spacingAndGlyphs">WHAT YOU</text>
    <text class="round c-blue" transform="translate(755 930) rotate(-90)" x="0" y="0" font-size="17" textLength="112" lengthAdjust="spacingAndGlyphs">CAN'T CHANGE</text>
    <text class="round c-red" transform="translate(798 925) rotate(-90)" x="0" y="0" font-size="51" textLength="110" lengthAdjust="spacingAndGlyphs">GO FOR A</text>
    <text class="round c-red" transform="translate(846 1000) rotate(-90)" x="0" y="0" font-size="62" textLength="185" lengthAdjust="spacingAndGlyphs">BIKE RIDE</text>

    <text class="round c-brown" x="152" y="895" font-size="31" textLength="206" lengthAdjust="spacingAndGlyphs">MAKE YOURSELF</text>
    <text class="round c-brown" x="152" y="927" font-size="37" textLength="206" lengthAdjust="spacingAndGlyphs">A CUP OF TEA</text>
    <text class="round c-grey" x="365" y="890" font-size="23" textLength="167" lengthAdjust="spacingAndGlyphs">TAKE A CLASS AT</text>
    <text class="round c-grey" x="365" y="927" font-size="43" textLength="167" lengthAdjust="spacingAndGlyphs">THE GYM</text>
    <text class="round c-red" x="152" y="960" font-size="25" textLength="176" lengthAdjust="spacingAndGlyphs">LISTEN TO A GUIDED</text>
    <text class="round c-red" x="152" y="994" font-size="34" textLength="176" lengthAdjust="spacingAndGlyphs">RELAXATION</text>
    <text class="light c-pink" x="332" y="998" font-size="88" textLength="142" lengthAdjust="spacingAndGlyphs">MP3</text>
    <text class="round c-pink" x="480" y="969" font-size="43" textLength="157" lengthAdjust="spacingAndGlyphs">DISCONNECT</text>
    <text class="medium c-pink" x="480" y="995" font-size="28" textLength="157" lengthAdjust="spacingAndGlyphs">FROM TECHNOLOGY</text>
    <text class="round c-leaf" x="645" y="948" font-size="23" textLength="111" lengthAdjust="spacingAndGlyphs">WATCH THE</text>
    <text class="round c-leaf" x="645" y="972" font-size="28" textLength="111" lengthAdjust="spacingAndGlyphs">CLOUDS</text>
    <text class="round c-leaf" x="690" y="995" font-size="28" textLength="66" lengthAdjust="spacingAndGlyphs">GO BY</text>

    <text class="round c-pink" x="152" y="1060" font-size="66" textLength="228" lengthAdjust="spacingAndGlyphs">LOOK AT A</text>
    <text class="light c-pink" x="152" y="1097" font-size="47" textLength="228" lengthAdjust="spacingAndGlyphs">WORK OF ART</text>
    <text class="round c-blue" x="390" y="1047" font-size="51" textLength="138" lengthAdjust="spacingAndGlyphs">READ A</text>
    <text class="round c-blue" x="390" y="1097" font-size="69" textLength="138" lengthAdjust="spacingAndGlyphs">BOOK</text>
    <text class="bold c-sage" x="537" y="1022" font-size="25" textLength="221" lengthAdjust="spacingAndGlyphs">DE-CLUTTER A DRAWER</text>
    <text class="round c-leaf" transform="translate(548 1100) rotate(-90)" x="0" y="0" font-size="13" textLength="60" lengthAdjust="spacingAndGlyphs">TAKE A LONG</text>
    <text class="round c-leaf" transform="translate(578 1100) rotate(-90)" x="0" y="0" font-size="37" textLength="55" lengthAdjust="spacingAndGlyphs">DRIVE</text>
    <text class="round c-orange" x="590" y="1057" font-size="37" textLength="170" lengthAdjust="spacingAndGlyphs">COLOUR IN</text>
  </g>

  <g class="brand">
    <circle class="brand-mark" cx="810" cy="1036" r="30"/>
    <text class="round c-grey brand-name" x="590" y="1082" font-size="25" textLength="190" lengthAdjust="spacingAndGlyphs">Willowbank Haven</text>
    <text class="round c-grey brand-strapline" x="590" y="1101" font-size="16" textLength="218" lengthAdjust="spacingAndGlyphs">counselling &amp; coaching for mums</text>
    <text class="round c-green brand-web" x="650" y="1124" font-size="12" textLength="165" lengthAdjust="spacingAndGlyphs">www.willowbankhaven.com.au</text>
  </g>
</svg>
</body>
</html>
```